Brightway Haul & Repair Services, are a company that offers a 'one stop shop' pre-move clean up a

I have already selected a logo which I would like on the front of the business cards along with phone numbers, web address and email which are:
0419574302
www.brightwayhaul.com.au
brightwayhaulrepair@mailbox.example

On the back of the card I would like to list some of the types of service we offer (clean - move - repairs/maintenance) which are:
CLEAN - windows, gutters, solar panels, driveways/paths, carpets.
MOVE - Small/medium size house/office moves, large item pick-up & delivery, yard clean-up and removal.
General maintenance and repairs.

I would like the blue logo on a gray background.

Thanks

```html
<!DOCTYPE html>
<html lang="en">
<head>
<meta charset="utf-8">
<title>Brightway Haul &amp; Repair Services – Business Card</title>
<link rel="stylesheet" href="https://fonts.googleapis.com/css2?family=Arimo:wght@400;700&family=Lexend+Exa:wght@300;700&display=swap">
<style>
  :root {
    --card-grey: #e6e7e8;
    --brand-blue: #3471b8;
    --label-blue: #3a73b8;
    --text-grey: #58595b;
    --white: #ffffff;
  }
  * { margin: 0; padding: 0; box-sizing: border-box; }
  html, body {
    width: 1012px;
    height: 1200px;
    overflow: hidden;
    background: var(--white);
  }
  .card {
    position: relative;
    width: 1012px;
    height: 1200px;
  }
  .card-front {
    position: absolute;
    left: 0; top: 0;
    width: 1012px;
    height: 598px;
    background: var(--card-grey);
  }
  .card-back {
    position: absolute;
    left: 0; top: 604px;
    width: 1012px;
    height: 596px;
    background: var(--brand-blue);
    color: var(--white);
    font-family: "Lexend Exa", sans-serif;
    text-align: center;
  }
  .brand-name {
    position: absolute;
    left: 0; right: 0;
    top: 175px;
    text-align: center;
    font-family: "Arimo", sans-serif;
    font-weight: 700;
    font-size: 54px;
    line-height: 1.15;
    color: var(--brand-blue);
    text-transform: uppercase;
  }
  .contact-list {
    position: absolute;
    left: 0; right: 0;
    top: 462px;
    list-style: none;
    text-align: center;
    font-family: "Arimo", sans-serif;
    font-size: 25px;
    line-height: 33.5px;
    color: var(--text-grey);
  }
  .contact-label {
    font-weight: 700;
    color: var(--label-blue);
  }
  .service-tabs {
    position: absolute;
    left: 84px;
    top: 174px;
    width: 844px;
    height: 48px;
    border-radius: 24px;
    background: var(--white);
    color: var(--brand-blue);
    font-weight: 700;
    font-size: 23px;
    line-height: 48px;
    white-space: nowrap;
    word-spacing: 4px;
  }
  .service-tabs .divider { margin: 0 22px; }
  .service-list {
    position: absolute;
    left: 0; right: 0;
    top: 248px;
    font-weight: 300;
    font-size: 22px;
    line-height: 47.5px;
    white-space: nowrap;
    letter-spacing: -0.3px;
  }
  .service-list p { margin: 0; }
  .service-heading { font-weight: 700; font-size: 25px; }
  .service-general { font-weight: 700; }
  .abn {
    position: absolute;
    left: 0; right: 0;
    top: 535px;
    font-weight: 700;
    font-size: 32px;
    letter-spacing: 1px;
  }
</style>
</head>
<body>
<main class="card">
  <section class="card-front">
    <h1 class="brand-name">Brightway Haul &amp;<br>Repair Services</h1>
    <ul class="contact-list">
      <li><span class="contact-label">Call:</span> Dean or Marco</li>
      <li><span class="contact-label">Phone:</span> 0419574302</li>
      <li><span class="contact-label">Website:</span> www.brightwayhaul.com.au</li>
      <li><span class="contact-label">E-mail:</span> brightwayhaulrepair@mailbox.example</li>
    </ul>
  </section>
  <section class="card-back">
    <div class="service-tabs">CLEAN<span class="divider">I</span>MOVE<span class="divider">I</span>REPAIRS/MAINTENANCE</div>
    <div class="service-list">
      <p><span class="service-heading">CLEAN</span> – Windows, Gutters, Solar panels,</p>
      <p>Driveways/Paths, Carpets.</p>
      <p><span class="service-heading">MOVE</span> – Small/Medium size House/Office moves</p>
      <p>Large item pick-up &amp; delivery, Yard clean-up and removal.</p>
      <p class="service-general">General maintenance and repairs.</p>
    </div>
    <div class="abn">ABN 48193027615</div>
  </section>
</main>
</body>
</html>
```